Paying WELL above market rates to find the very best Powerpoint Designer for keynote presentations..

Large cap tech company on the west coast is looking to bring a fresh and innovative new look to a series of keynote presentations. There will be 4 x 30 slide decks over the next 3 months. We are the whale customer you want to land!...We are prepared to pay WELL about market rates to attract the very best designers to work on our project.

Attached are the slides I would like repainted... we did these internally, but I need them to be redesigned....

Target Market(s)

Enterprise Corporate

Industry/Entity Type

It Company

```html
<!DOCTYPE html>
<html lang="en">
<head>
<meta charset="utf-8">
<title>Presentation Slide</title>
<link href="https://fonts.googleapis.com/css2?family=Carlito:wght@400;700&display=swap" rel="stylesheet">
<style>
  :root {
    --orange: #f5821f;
    --header-rule: #6b6b6b;
    --footer-grey: #5a5a5a;
    --text-grey: #7f7f7f;
    --chevron-light: #a6a6a6;
    --chevron-mid: #595959;
    --chevron-dark: #262626;
    --chevron-soft: #808080;
    --white: #ffffff;
    --page-bg: #ffffff;
  }
  html, body {
    margin: 0;
    padding: 0;
    width: 1200px;
    height: 900px;
    overflow: hidden;
    background: var(--page-bg);
  }
  .slide {
    position: relative;
    width: 1200px;
    height: 900px;
    overflow: hidden;
    background: var(--page-bg);
    font-family: "Carlito", "Calibri", sans-serif;
  }
  .header-band {
    position: absolute;
    left: 0; top: 0;
    width: 1200px;
    height: 66px;
    background: var(--orange);
    border-bottom: 4px solid var(--header-rule);
  }
  .slide-title {
    position: absolute;
    left: 14px; top: 10px;
    margin: 0;
    color: var(--white);
    font-size: 34px;
    font-weight: 700;
    letter-spacing: 0.2px;
  }
  .header-badge {
    position: absolute;
    left: 1086px; top: 20px;
    width: 100px; height: 100px;
  }
  .backdrop-art {
    position: absolute;
    left: 800px; top: 100px;
    width: 400px; height: 755px;
    border-radius: 140px 140px 20px 20px;
    background: radial-gradient(ellipse at 60% 40%, rgba(200,200,200,0.28), rgba(235,235,235,0.12) 70%, rgba(255,255,255,0) 100%);
  }
  .feature {
    position: absolute;
    left: 90px;
    width: 1040px;
    height: 112px;
  }
  .feature-chevron {
    position: absolute;
    left: 0; top: 0;
    width: 203px; height: 110px;
  }
  .feature-body {
    position: absolute;
    left: 238px;
    top: -14px;
  }
  .feature-subtitle {
    margin: 0;
    color: var(--orange);
    font-size: 26px;
    font-weight: 700;
    line-height: 34px;
  }
  .feature-text {
    margin: 2px 0 0;
    color: var(--text-grey);
    font-size: 20px;
    line-height: 34.5px;
    width: 800px;
  }
  .footer-band {
    position: absolute;
    left: 0; top: 855px;
    width: 1200px; height: 45px;
    background: var(--footer-grey);
  }
  .copyright {
    position: absolute;
    left: 9px; top: 10px;
    margin: 0;
    color: var(--white);
    font-size: 22px;
  }
  .page-number {
    position: absolute;
    left: 1108px; top: 824px;
    width: 68px; height: 68px;
    box-sizing: border-box;
    border-radius: 50%;
    border: 4px solid var(--white);
    background: var(--orange);
    color: var(--white);
    font-weight: 700;
    font-size: 24px;
    display: flex;
    align-items: center;
    justify-content: center;
  }
</style>
</head>
<body>
<div class="slide">
  <div class="backdrop-art" role="img" aria-label="Faint large trophy silhouette in the background"></div>

  <header class="header-band">
    <h1 class="slide-title">PERSENTATION TITLE HERE</h1>
  </header>
  <svg class="header-badge" viewBox="0 0 100 100" aria-hidden="true" style="top:-33px">
    <circle cx="50" cy="50" r="48" fill="#6b6b6b"/>
    <circle cx="50" cy="47" r="45" fill="var(--orange)"/>
    <g fill="#ffffff">
      <path d="M36 34 h28 v6 c0 10 -6 16 -14 16 c-8 0 -14 -6 -14 -16 z"/>
      <path d="M36 37 h-7 c0 8 4 12 9 12 v-3 c-3 0 -5 -3 -5 -6 h3 z"/>
      <path d="M64 37 h7 c0 8 -4 12 -9 12 v-3 c3 0 5 -3 5 -6 h-3 z"/>
      <rect x="47" y="55" width="6" height="8"/>
      <rect x="40" y="63" width="20" height="5" rx="1"/>
    </g>
  </svg>

  <section class="feature" style="top:157px">
    <svg class="feature-chevron" viewBox="0 0 203 110" aria-hidden="true">
      <polygon points="0,0 167,0 203,55 167,110 0,110 36,55" fill="var(--chevron-light)"/>
      <rect x="83" y="37" width="37" height="26" rx="2" fill="none" stroke="#fff" stroke-width="5"/>
      <rect x="96" y="63" width="11" height="6" fill="#fff"/>
      <rect x="90" y="69" width="23" height="3" fill="#fff"/>
    </svg>
    <div class="feature-body">
      <h2 class="feature-subtitle">Subtitle Here</h2>
      <p class="feature-text">Description Text here Description Text here Description Text here Description Text here Description Text here Description Text here Description Text here Description Text here Description Text here Description Text here Description Text here Description Text here</p>
    </div>
  </section>

  <section class="feature" style="top:345px">
    <svg class="feature-chevron" viewBox="0 0 203 110" aria-hidden="true">
      <polygon points="0,0 167,0 203,55 167,110 0,110 36,55" fill="var(--chevron-mid)"/>
      <g transform="rotate(45 102 55)" fill="#fff">
        <path d="M102 33 c6 5 8 12 8 20 v14 h-16 v-14 c0 -8 2 -15 8 -20 z"/>
        <path d="M94 58 l-6 8 v6 l6 -4 z"/>
        <path d="M110 58 l6 8 v6 l-6 -4 z"/>
        <path d="M98 68 h8 l-4 8 z"/>
      </g>
      <circle cx="102" cy="52" r="3" fill="var(--chevron-mid)"/>
    </svg>
    <div class="feature-body">
      <h2 class="feature-subtitle">Subtitle Here</h2>
      <p class="feature-text">Description Text here Description Text here Description Text here Description Text here Description Text here Description Text here Description Text here Description Text here Description Text here Description Text here Description Text here Description Text here</p>
    </div>
  </section>

  <section class="feature" style="top:502px">
    <svg class="feature-chevron" viewBox="0 0 203 110" aria-hidden="true">
      <polygon points="0,0 167,0 203,55 167,110 0,110 36,55" fill="var(--chevron-dark)"/>
      <g fill="#fff">
        <path d="M84 42 h14 v14 c0 8 -4 13 -11 15 l-2 -4 c4 -2 6 -5 6 -9 h-7 z"/>
        <path d="M104 42 h14 v14 c0 8 -4 13 -11 15 l-2 -4 c4 -2 6 -5 6 -9 h-7 z"/>
      </g>
    </svg>
    <div class="feature-body">
      <h2 class="feature-subtitle">Subtitle Here</h2>
      <p class="feature-text">Description Text here Description Text here Description Text here Description Text here Description Text here Description Text here Description Text here Description Text here Description Text here Description Text here Description Text here Description Text here</p>
    </div>
  </section>

  <section class="feature" style="top:657px">
    <svg class="feature-chevron" viewBox="0 0 203 110" aria-hidden="true">
      <polygon points="0,0 167,0 203,55 167,110 0,110 36,55" fill="var(--chevron-soft)"/>
      <path d="M88 38 h28 v16 c0 11 -6 17 -14 21 c-8 -4 -14 -10 -14 -21 z" fill="#fff"/>
      <path d="M102 43 h9 v11 c0 7 -4 11 -9 14 z" fill="var(--chevron-soft)"/>
    </svg>
    <div class="feature-body">
      <h2 class="feature-subtitle">Subtitle Here</h2>
      <p class="feature-text">Description Text here Description Text here Description Text here Description Text here Description Text here Description Text here Description Text here Description Text here Description Text here Description Text here Description Text here Description Text here</p>
    </div>
  </section>

  <footer class="footer-band">
    <p class="copyright">Copyright text here</p>
  </footer>
  <div class="page-number">01</div>
</div>
</body>
</html>
```